lunetra.com redesign

We are a successful web hosting company that has been around since 1999 with 10,000 customers managing 2,000 websites and 12,000 domain names. Our challenge - we are losing ground because our site is getting old, our pricing is not competitive and our feature set needs to change to match the new world of mobile centric everything. We want to reach out to all of the domain names that we don't host websites for. We believe that if we designed a new site that focuses on bringing home all of those externally hosted websites to our own web hosting company that we would have a solid future. We need to compete against mopwizzle.com, vantrimble.com, kerbloom.com, zinqhut.com, nolvark.com, brimfolk.com, quorvane.com, welbix.com and 100,000 others. We need to simplify our message with clean design, focused pages, easy decision making processes for the consumer. We use WHMCS for the background provisioning and billing so we can pretty much manage any kind of pricing model and discounted promotion packages.
I would prefer Twitter bootstrap CSS based responsive design.

Reason: I was away on vacation for 2 weeks - I just got back - I need time to fairly review all submissions - thank you for your patience. Dorian Fenwick Lunetra.com

Thanks to all who submitted sample designs - unfortunately most of them were nothing much more than already available templates with some of my current content and logo added to them. I will try to be more specific to reduce the number of choices. I need the template be fully compatible with WHMCS and Wordpress if you can't make it work with WHMCS directly. Another question I have to ask is -"exactly what am I getting for my $500.00 - is it just a PSD template or actual integration of that theme into WHMCS or Wordpress?"  I don't expect anyone to create new content for the site at that price. What do you charge if  you are able to create content or get directly involved in the site implementation of that template?

```html
<!DOCTYPE html>
<html lang="en">
<head>
<meta charset="utf-8">
<title>Lunetra — Web Hosting &amp; Domains</title>
<link href="https://fonts.googleapis.com/css2?family=Ubuntu:wght@400;500;700&family=Open+Sans:wght@400;600&display=swap" rel="stylesheet">
<style>
:root{
  --orange:#e8501e;
  --orange-dark:#c8400f;
  --blue:#2463b6;
  --blue-deep:#1e58a8;
  --nav-blue:#1f60b5;
  --ink:#2a2a2a;
  --ink-soft:#555;
  --charcoal-2:#333;
  --line:#dcdcdc;
  --page:#f4f4f4;
  --white:#fff;
  --card-a:#1e58a8;
  --card-b:#e8501e;
  --card-c:#f2b705;
  --card-d:#3c9a4a;
  --card-e:#7a7a7a;
}
*{box-sizing:border-box;margin:0;padding:0}
html,body{width:1200px;height:2727px;overflow:hidden}
body{font-family:"Open Sans",Arial,sans-serif;color:var(--ink);background:var(--page);position:relative}
a{color:inherit;text-decoration:none}
.wrap{position:relative;width:836px;margin:0 auto;height:100%}

/* top utility bar */
.utility{height:22px;background:#1b1b1b;border-bottom:1px solid #333}
.utility ul{list-style:none;position:absolute;right:0;top:4px;display:flex;font-size:10px;color:#9a9a9a}
.utility li{padding:0 11px;border-left:1px solid #444}
.utility li:first-child{border-left:none}

/* header */
.masthead{height:93px;background:linear-gradient(#2e2e2e,#242424)}
.brand{position:absolute;left:0;top:20px;font-family:"Ubuntu",sans-serif;font-weight:700;font-size:48px;color:var(--white);letter-spacing:-1px}
.call{position:absolute;left:475px;top:34px;display:flex;align-items:center;gap:10px;color:var(--white);font-size:14px}
.btn{display:inline-block;font-family:"Ubuntu",sans-serif;font-weight:500;font-size:11px;color:var(--white);text-transform:uppercase;text-align:center}
.btn-login{position:absolute;left:668px;top:29px;width:76px;height:30px;line-height:30px;background:var(--orange)}
.btn-signup{position:absolute;left:752px;top:29px;width:84px;height:30px;line-height:30px;background:var(--blue)}

/* navigation */
.mainnav{height:43px;background:var(--nav-blue);border-top:1px solid #3b7bd0}
.mainnav ul{list-style:none;display:flex;height:43px;font-family:"Ubuntu",sans-serif;font-size:14px;color:var(--white)}
.mainnav li{line-height:43px;padding:0 21px}
.mainnav li.active{background:#174f99}

/* hero */
.hero{height:487px;position:relative;background:linear-gradient(90deg,#1c1c1c,#3a3836 45%,#2a2826 70%,#1a1a1a)}
.hero-photo{position:absolute;inset:0;background:linear-gradient(180deg,rgba(0,0,0,.15),rgba(0,0,0,.45))}
.slide-arrow{position:absolute;top:165px;width:48px;height:48px;border:2px solid var(--orange);border-radius:50%}
.slide-arrow.prev{left:41px}
.slide-arrow.next{right:38px}
.slide-arrow svg{position:absolute;left:13px;top:13px}
.screen{position:absolute;left:0;top:88px;width:358px;height:245px;background:linear-gradient(135deg,#f05a22,#c9370b);border:10px solid #111;border-radius:6px 6px 0 0}
.screen-chin{position:absolute;left:0;top:333px;width:358px;height:30px;background:linear-gradient(#e4e4e4,#bdbdbd);border-radius:0 0 6px 6px}
.screen-stand{position:absolute;left:135px;top:363px;width:88px;height:36px;background:linear-gradient(#cfcfcf,#9a9a9a);clip-path:polygon(20% 0,80% 0,100% 100%,0 100%)}
.offer{position:absolute;left:454px;top:87px;width:404px;height:286px;background:rgba(30,30,30,.88);border:1px solid #444;color:var(--white);padding:22px 28px}
.offer .tag{position:absolute;left:28px;top:24px;width:44px;height:60px;background:var(--white);color:var(--ink);font-family:"Ubuntu",sans-serif;font-weight:700;font-size:12px;text-align:center;padding-top:18px;clip-path:polygon(0 0,100% 0,100% 100%,50% 80%,0 100%)}
.offer h2{margin-left:60px;font-family:"Ubuntu",sans-serif;font-weight:500;font-size:38px;line-height:38px}
.offer h3{margin-left:60px;font-family:"Ubuntu",sans-serif;font-weight:400;font-size:25px;line-height:28px;color:#ddd}
.offer p{margin-top:28px;font-size:12px;color:#bbb;line-height:18px}
.offer ul{list-style:none;margin-top:10px;display:grid;grid-template-columns:140px 140px;row-gap:6px;font-size:13px}
.offer li::before{content:"✔";color:#8bc34a;margin-right:6px}
.btn-cta{margin-top:16px;width:140px;height:34px;line-height:34px;background:var(--orange);font-size:12px}

/* features band */
.features{height:337px;background:linear-gradient(90deg,var(--orange-dark),var(--orange) 50%,#ec5f2a)}
.features .grid{display:grid;grid-template-columns:1fr 1fr;height:100%;padding-top:14px}
.feature{position:relative;padding:40px 0 0 91px;height:146px;color:var(--white)}
.feature:nth-child(2n){border-left:1px solid rgba(255,255,255,.3);padding-left:105px}
.feature:nth-child(1),.feature:nth-child(2){border-bottom:1px solid rgba(255,255,255,.3)}
.feature:nth-child(3),.feature:nth-child(4){padding-top:44px}
.feature svg{position:absolute;left:27px;top:38px}
.feature:nth-child(2n) svg{left:42px}
.feature:nth-child(3) svg,.feature:nth-child(4) svg{top:42px}
.feature h3{font-family:"Ubuntu",sans-serif;font-weight:400;font-size:20px;line-height:24px}
.feature p{font-size:11px;margin-top:16px;line-height:16px;max-width:320px}

/* pricing */
.pricing{height:482px;background:var(--page)}
.section-title{font-family:"Ubuntu",sans-serif;font-weight:400;text-align:center}
.pricing .section-title{padding-top:50px;font-size:33px;color:var(--blue)}
.plans{display:grid;grid-template-columns:repeat(4,195px);column-gap:18px;margin-top:28px}
.plan{background:var(--white);border:1px solid var(--line);height:287px;text-align:center}
.plan h3{height:40px;line-height:40px;background:var(--charcoal-2);color:var(--white);font-family:"Ubuntu",sans-serif;font-weight:400;font-size:16px}
.plan .price{height:50px;border-bottom:1px solid var(--line);padding-top:8px;color:#888;font-size:17px;line-height:18px}
.plan .price small{display:block;font-size:8px;color:#666}
.plan .row{height:50px;border-bottom:1px solid var(--line);font-size:10px;color:#666;display:flex;align-items:center;justify-content:center;line-height:13px}
.plan .row.one{height:38px}
.btn-choose{margin-top:14px;width:110px;height:30px;line-height:30px;background:var(--blue);border-radius:2px;font-size:13px;text-transform:none;font-family:"Open Sans",sans-serif;font-weight:600}

/* free services */
.services{height:400px;background:var(--blue-deep)}
.services .section-title{padding-top:42px;font-size:30px;color:var(--white)}
.service-list{display:grid;grid-template-columns:repeat(4,218px);margin:62px 0 0 -18px;text-align:center;color:var(--white)}
.service .badge{width:80px;height:80px;border-radius:50%;background:#1a4c93;margin:0 auto;position:relative}
.service .badge.on{background:var(--white);box-shadow:0 0 0 5px var(--blue-deep),0 0 0 8px var(--white)}
.service .badge svg{position:absolute;left:22px;top:22px}
.service h3{font-family:"Ubuntu",sans-serif;font-weight:400;font-size:16px;margin-top:20px}
.service p{font-size:11px;line-height:15px;margin:8px auto 0;width:170px;color:#dfe8f6}

/* about grid */
.about{height:787px;background:var(--page)}
.about .section-title{padding-top:42px;font-size:30px;color:var(--orange)}
.about-grid{display:grid;grid-template-columns:1fr 1fr;margin-top:50px}
.about-item{padding:18px 20px 18px 0;border-bottom:1px solid #e2e2e2}
.about-item:nth-child(2n){border-left:1px solid #e2e2e2;padding-left:24px}
.about-item:nth-child(1),.about-item:nth-child(2){height:161px}
.about-item:nth-child(3),.about-item:nth-child(4){height:144px}
.about-item:nth-child(5),.about-item:nth-child(6){height:156px}
.about-item:nth-child(7),.about-item:nth-child(8){height:170px;border-bottom:none}
.about-item h3{font-family:"Ubuntu",sans-serif;font-weight:400;font-size:20px;color:var(--blue)}
.about-item p{font-size:11px;line-height:15.5px;color:var(--ink-soft);margin-top:8px}
.about-item a{color:var(--orange)}

/* footer */
.site-footer{height:78px;background:#111;color:#aaa}
.footer-links{position:absolute;left:0;top:20px;display:flex;list-style:none;font-size:10px}
.footer-links li{padding:0 14px;border-left:1px solid #444}
.footer-links li:first-child{padding-left:0;border-left:none}
.pay-badge{position:absolute;right:0;top:7px;width:146px;height:38px;background:var(--white);border:2px solid #ccc}
.copyright{position:absolute;left:0;right:0;bottom:8px;text-align:center;font-size:9px;color:#888}
</style>
</head>
<body>

<div class="utility"><div class="wrap">
  <ul><li>Company</li><li>Partners</li><li>Support</li><li>Contact Us</li><li>Shopping Cart</li><li>References</li><li>Pricing</li></ul>
</div></div>

<header class="masthead"><div class="wrap">
  <a class="brand" href="#">lunetra</a>
  <div class="call">
    <svg width="26" height="26" viewBox="0 0 26 26"><circle cx="13" cy="13" r="12" fill="none" stroke="#e8501e" stroke-width="2"/><path d="M9 7l3 3-2 2c1 2 2 3 4 4l2-2 3 3-2 2c-5-1-9-5-10-10z" fill="#e8501e"/></svg>
    <span>Call: (888) 555-0142</span>
  </div>
  <a class="btn btn-login" href="#">Log in</a>
  <a class="btn btn-signup" href="#">Sign up</a>
</div></header>

<nav class="mainnav"><div class="wrap">
  <ul><li class="active">Home</li><li>Domain Name Center</li><li>Web Site Hosting Center</li><li>S.E.O. Toolkit</li><li>Support</li><li>Client Area</li></ul>
</div></nav>

<section class="hero">
  <div class="hero-photo" role="img" aria-label="Dark photograph of server racks in a data centre"></div>
  <a class="slide-arrow prev" href="#"><svg width="18" height="18" viewBox="0 0 18 18"><path d="M12 2L5 9l7 7" fill="none" stroke="#e8501e" stroke-width="2"/></svg></a>
  <a class="slide-arrow next" href="#"><svg width="18" height="18" viewBox="0 0 18 18"><path d="M6 2l7 7-7 7" fill="none" stroke="#e8501e" stroke-width="2"/></svg></a>
  <div class="wrap">
    <div class="screen" role="img" aria-label="Desktop monitor playing a brand video on an orange screen"></div>
    <div class="screen-chin"></div>
    <div class="screen-stand"></div>
    <div class="offer">
      <div class="tag">FREE</div>
      <h2>DOMAIN NAME</h2>
      <h3>with every new hosting</h3>
      <p>When you want the ultimate in website performance,<br>security, and control, this is it.</p>
      <ul><li>Domain name</li><li>SiteBuilder</li><li>Hosting</li><li>More</li></ul>
      <a class="btn btn-cta" href="#">Sign up now!</a>
    </div>
  </div>
</section>

<section class="features"><div class="wrap"><div class="grid">
  <div class="feature">
    <svg width="50" height="50" viewBox="0 0 50 50"><path d="M14 22v-6a9 9 0 0118 0v6" fill="none" stroke="#fff" stroke-width="4"/><rect x="8" y="22" width="30" height="24" rx="3" fill="#fff"/><circle cx="23" cy="33" r="3" fill="#e8501e"/></svg>
    <h3>Secure Your Domin Name</h3>
    <p>Register, Renew, Transfer or Search your Domin Name</p>
  </div>
  <div class="feature">
    <svg width="46" height="44" viewBox="0 0 46 44"><rect x="2" y="2" width="42" height="38" rx="3" fill="none" stroke="#fff" stroke-width="3"/><line x1="2" y1="11" x2="44" y2="11" stroke="#fff" stroke-width="3"/><text x="23" y="30" font-size="11" font-family="Ubuntu,sans-serif" font-weight="700" fill="#fff" text-anchor="middle">www</text></svg>
    <h3>Web Site Hosting</h3>
    <p>Reliable, affordable options. Real people -real support.</p>
  </div>
  <div class="feature">
    <svg width="50" height="48" viewBox="0 0 50 48"><rect x="2" y="2" width="42" height="34" rx="3" fill="none" stroke="#fff" stroke-width="3"/><line x1="2" y1="10" x2="44" y2="10" stroke="#fff" stroke-width="3"/><circle cx="36" cy="36" r="8" fill="#e8501e" stroke="#fff" stroke-width="3"/></svg>
    <h3>Effective Websites Development</h3>
    <p>StepsSites Web Builder, Small Business Bundle and Custom Design</p>
  </div>
  <div class="feature">
    <svg width="46" height="48" viewBox="0 0 46 48"><rect x="8" y="2" width="30" height="22" rx="2" fill="none" stroke="#fff" stroke-width="3"/><rect x="2" y="24" width="42" height="20" rx="2" fill="#fff"/><rect x="14" y="30" width="18" height="4" fill="#e8501e"/></svg>
    <h3>Market Your Web Site</h3>
    <p>Professional implementation of Search Engine Positioning</p>
  </div>
</div></div></section>

<section class="pricing"><div class="wrap">
  <h2 class="section-title">Choose a Hosting Package</h2>
  <div class="plans">
    <div class="plan"><h3>E-Lite</h3><div class="price">$90.00<small>Annual Price</small></div><div class="row one">100 MB Annual Traffic</div><div class="row">Unlimited<br>Email Account</div><div class="row">Domin Name<br>Included</div><a class="btn btn-choose" href="#">Choose</a></div>
    <div class="plan"><h3>E-200</h3><div class="price">$149.00<small>Annual Price</small></div><div class="row one">200 MB Annual Traffic</div><div class="row">Unlimited<br>Email Account</div><div class="row">Domin Name<br>Included</div><a class="btn btn-choose" href="#">Choose</a></div>
    <div class="plan"><h3>E-500</h3><div class="price">$249.00<small>Annual Price</small></div><div class="row one">500 MB Annual Traffic</div><div class="row">Unlimited<br>Email Account</div><div class="row">Domin Name<br>Included</div><a class="btn btn-choose" href="#">Choose</a></div>
    <div class="plan"><h3>E-1000</h3><div class="price">$549.00<small>Annual Price</small></div><div class="row one">1000 MB Annual Traffic</div><div class="row">Unlimited<br>Email Account</div><div class="row">Domin Name<br>Included</div><a class="btn btn-choose" href="#">Choose</a></div>
  </div>
</div></section>

<section class="services"><div class="wrap">
  <h2 class="section-title">Get these free Services with all Accounts</h2>
  <div class="service-list">
    <div class="service">
      <div class="badge on"><svg width="36" height="36" viewBox="0 0 36 36"><rect x="4" y="2" width="18" height="24" fill="none" stroke="#1e58a8" stroke-width="3"/><rect x="14" y="10" width="18" height="24" fill="#fff" stroke="#1e58a8" stroke-width="3"/><path d="M18 20h10M24 16l4 4-4 4" fill="none" stroke="#1e58a8" stroke-width="2"/></svg></div>
      <h3>EasyTransfer</h3><p>Switching to Lunetra from another host is easy: sit back while we take care of everything.</p>
    </div>
    <div class="service">
      <div class="badge"><svg width="36" height="36" viewBox="0 0 36 36"><rect x="2" y="6" width="32" height="24" rx="2" fill="none" stroke="#fff" stroke-width="2.5"/><line x1="2" y1="12" x2="34" y2="12" stroke="#fff" stroke-width="2.5"/><text x="18" y="25" font-size="8" font-family="Ubuntu,sans-serif" font-weight="700" fill="#fff" text-anchor="middle">www</text></svg></div>
      <h3>Site Builder</h3><p>With SiteBuilder, you can build your website with drag-and-drop simplicity.</p>
    </div>
    <div class="service">
      <div class="badge"><svg width="36" height="36" viewBox="0 0 36 36"><rect x="4" y="4" width="28" height="28" rx="2" fill="none" stroke="#fff" stroke-width="2.5"/><circle cx="15" cy="20" r="7" fill="none" stroke="#fff" stroke-width="2.5"/><circle cx="15" cy="20" r="2" fill="#fff"/></svg></div>
      <h3>Installation</h3><p>Over 50 essential scripts for building your website installed in minutes with a click.</p>
    </div>
    <div class="service">
      <div class="badge"><svg width="36" height="36" viewBox="0 0 36 36"><rect x="4" y="2" width="18" height="24" fill="none" stroke="#fff" stroke-width="2.5"/><rect x="14" y="10" width="18" height="24" fill="#1a4c93" stroke="#fff" stroke-width="2.5"/><path d="M18 22h10M24 18l4 4-4 4" fill="none" stroke="#fff" stroke-width="2"/></svg></div>
      <h3>BeFound</h3><p>We include search engine positioning with every plan, so your customers can find your website.</p>
    </div>
  </div>
</div></section>

<section class="about"><div class="wrap">
  <h2 class="section-title">Lunetra makes it easy to get online</h2>
  <div class="about-grid">
    <div class="about-item"><h3>About Lunetra</h3><p>As an Namewell-accredited registrar for more than 10 years, Lunetra is a leading provider of <a href="#">domain registration</a>, <a href="#">website hosting</a>, <a href="#">website design</a>, and <a href="#">email hosting</a> for small and medium-sized businesses. Lunetra has helped tens of thousands of businesses and individuals establish their web presence, build their websites, and drive revenue.</p></div>
    <div class="about-item"><h3>SiteBuilder</h3><p>Included free with every hosting plan, Lunetra's premium <a href="#">SiteBuilder</a> lets anyone easily create a business-quality website. Hundreds of professional templates are available.</p></div>
    <div class="about-item"><h3>Domain Registration</h3><p><a href="#">Registering a domain</a> is the first step in building your website. Choose from dozens of domain extensions such as .com, .net, .us, .tel, .biz, .org, .ca and .us. Lunetra offers competitive prices, easy domain search and registration, auto-renewal and domain transfers.</p></div>
    <div class="about-item"><h3>Business Solutions</h3><p>Lunetra provides a variety of business and marketing solutions for small business customers. Some of these products include <a href="#">Website Builder</a> and <a href="#">Business Hosting</a> bundles and our extensive <a href="#">Search Engine Optimization</a> tool kit.</p></div>
    <div class="about-item"><h3>Website Hosting</h3><p>Lunetra's <a href="#">website hosting plans</a> are fast, flexible and affordable. We offer plans to meet your varying bandwidth and disk space requirements. All web hosting plans include free setup, one-click install web applications, and SiteBuilder, our do-it-yourself website building tool. Create a strong online web presence with Lunetra hosting.</p></div>
    <div class="about-item"><h3>24/7 Customer Service</h3><p>All Lunetra products come with free 24/7 support. For more information about Lunetra customer support, visit the <a href="#">Support</a> section of this website.</p></div>
    <div class="about-item"><h3>Email Hosting</h3><p><a href="#">Email hosting</a> lets you create personalized email accounts at the domain of your choice. Custom email addresses are an important part of building your online brand identity and demonstrating that you are a professional, web-savvy business. Lunetra includes email hosting in all business plans.</p></div>
    <div class="about-item"><h3>More Reasons to Choose Lunetra</h3><p>As an award winning, premium provider of Internet services for small businesses and individuals, Lunetra offers best in class products, dedicated customer support and the highest service reliability available. Choose Lunetra and start building your website today.<br>Lunetra has been recognized as a leader in business <a href="#">domain name registration</a> and <a href="#">business hosting</a>. Read what others are saying about us here, <a href="#">here and here</a>.</p></div>
  </div>
</div></section>

<footer class="site-footer"><div class="wrap">
  <ul class="footer-links"><li>Terms of use</li><li>Dispute Policy</li><li>Disclaimer</li><li>Privacy Policy</li><li>Refund Policy</li><li>Lunetra Newsletter</li></ul>
  <svg class="pay-badge" role="img" aria-label="Accepted payment methods" viewBox="0 0 142 34" width="146" height="38">
    <rect x="4" y="3" width="40" height="8" rx="2" fill="var(--card-a)"/>
    <rect x="6" y="17" width="18" height="12" rx="2" fill="var(--card-b)"/>
    <rect x="28" y="17" width="18" height="12" rx="2" fill="var(--card-a)"/>
    <rect x="50" y="17" width="18" height="12" rx="2" fill="var(--card-c)"/>
    <rect x="72" y="17" width="18" height="12" rx="2" fill="var(--card-d)"/>
    <rect x="94" y="17" width="18" height="12" rx="2" fill="var(--card-e)"/>
    <rect x="116" y="17" width="18" height="12" rx="2" fill="var(--card-a)"/>
  </svg>
  <p class="copyright">Copyrights © 2014.All Rights Reserved</p>
</div></footer>

</body>
</html>
```